Communication and Marketing agency needs a new presentation card

We are a group of communication and marketing agencies specialized in companies that are in the logistics and industrial sector. The head agency is VELUNEX Grupo and the group consists of 4 agencies: VELUNEX Media, VELUNEX Digital, VELUNEX Research and PlanoDeImagenes. We hace 4 offices in Spain (Madrid, Barcelona, Valencia and Murcia). We are looking for a clean and attractive design that transmits our experience, brand presence in the market and knowledge to those who receive the card.It has to maintain the colors of the logo that is attached.
logistics and industrial sector
Marketing department
Clean and attractive design

```html
<!DOCTYPE html>
<html lang="en">
<head>
<meta charset="utf-8">
<title>VELUNEX Business Cards</title>
<link rel="stylesheet" href="https://fonts.googleapis.com/css2?family=Montserrat:wght@400;500;700&display=swap">
<style>
  :root {
    --page: #ffffff;
    --frame: #bdbdbd;
    --slate: #575756;
    --slate-deep: #4a4a49;
    --slate-band: #3f3f3e;
    --red: #bb1829;
    --red-deep: #7c0f1b;
    --white: #ffffff;
  }
  * { margin: 0; padding: 0; box-sizing: border-box; }
  html, body { width: 1200px; height: 1200px; overflow: hidden; background: var(--page); }
  body { font-family: "Montserrat", sans-serif; color: var(--white); position: relative; }
  .sheet { position: absolute; inset: 0; border: 3px solid var(--frame); }
  .card {
    position: absolute; width: 348px; height: 204px; overflow: hidden;
    background: var(--slate);
    box-shadow: -4px 7px 12px rgba(0,0,0,.28);
  }
  .card--front-a { left: 224px; top: 366px; }
  .card--front-b { left: 224px; top: 608px; }
  .card--back-a  { left: 646px; top: 365px; }
  .card--back-b  { left: 646px; top: 609px; }
  .card__shape { position: absolute; inset: 0; }
  .brand { position: absolute; font-weight: 500; line-height: 1; text-align: right; }
  .brand__name { display: block; font-size: 24px; letter-spacing: 1px; }
  .brand__unit { display: block; font-size: 14px; margin-top: 3px; }
  .card--front-a .brand, .card--front-b .brand { right: 29px; top: 28px; }
  .contacts { position: absolute; left: 24px; top: 112px; list-style: none; font-size: 9.5px; }
  .contacts li { display: flex; align-items: center; height: 17.3px; }
  .contacts svg { width: 6px; height: 6px; margin-right: 10px; fill: var(--white); }
  .person { position: absolute; left: 172px; top: 150px; }
  .person__name { font-size: 14.5px; font-weight: 700; line-height: 1; }
  .person__role { font-size: 4.5px; letter-spacing: 2.6px; margin-top: 2px; }
  .back__band { position: absolute; left: 0; right: 0; top: 0; height: 18px; background: var(--red); }
  .back__tab { position: absolute; left: 110px; width: 128px; top: 0; height: 31px; background: var(--slate-band); }
  .back__tab::before { content: ""; position: absolute; left: 0; right: 0; top: 0; height: 18px; background: var(--red-deep); }
  .back__url { position: absolute; left: 0; right: 0; bottom: 2px; font-size: 5.5px; font-weight: 500; text-align: center; }
  .back__foot { position: absolute; left: 110px; width: 128px; bottom: 0; height: 18px; background: var(--red); }
  .card--back-a .brand { left: 0; right: 0; top: 82px; margin: 0 auto; width: 130px; }
  .card--back-b .brand { left: 0; right: 0; top: 80px; margin: 0 auto; width: 150px; }
  .card--back-b .brand__name { font-size: 28px; }
  .card--back-b .brand__unit { font-size: 16px; }
</style>
</head>
<body>
<div class="sheet">

  <section class="card card--front-a">
    <svg class="card__shape" viewBox="0 0 348 204" aria-hidden="true">
      <polygon points="93,27 348,170 348,204" fill="var(--slate-deep)"/>
      <polygon points="0,77 93,27 348,204 0,204" fill="var(--red)"/>
    </svg>
    <div class="brand"><span class="brand__name">VELUNEX</span><span class="brand__unit">Digital</span></div>
    <ul class="contacts">
      <li><svg viewBox="0 0 10 10"><rect x="1" y="2" width="8" height="6" rx="1"/></svg>your@email.com</li>
      <li><svg viewBox="0 0 10 10"><path d="M2 1h2l1 2-1 1a5 5 0 0 0 2 2l1-1 2 1v2c-4 0-7-3-7-7z"/></svg>+11111xxx</li>
      <li><svg viewBox="0 0 10 10"><path d="M5 0a3.5 3.5 0 0 1 3.5 3.5C8.5 6 5 10 5 10S1.5 6 1.5 3.5A3.5 3.5 0 0 1 5 0z"/></svg>your place company</li>
      <li><svg viewBox="0 0 10 10"><circle cx="5" cy="5" r="4.5"/></svg>www.yourwebsite.com</li>
    </ul>
    <div class="person"><div class="person__name">YOUR NAME</div><div class="person__role">JOB DESCRIPTION</div></div>
  </section>

  <section class="card card--front-b">
    <svg class="card__shape" viewBox="0 0 348 204" aria-hidden="true">
      <polygon points="93,27 348,170 348,204" fill="var(--slate-deep)"/>
      <polygon points="0,77 93,27 348,204 0,204" fill="var(--red)"/>
    </svg>
    <div class="brand"><span class="brand__name">VELUNEX</span><span class="brand__unit">Research</span></div>
    <ul class="contacts">
      <li><svg viewBox="0 0 10 10"><rect x="1" y="2" width="8" height="6" rx="1"/></svg>your@email.com</li>
      <li><svg viewBox="0 0 10 10"><path d="M2 1h2l1 2-1 1a5 5 0 0 0 2 2l1-1 2 1v2c-4 0-7-3-7-7z"/></svg>+11111xxx</li>
      <li><svg viewBox="0 0 10 10"><path d="M5 0a3.5 3.5 0 0 1 3.5 3.5C8.5 6 5 10 5 10S1.5 6 1.5 3.5A3.5 3.5 0 0 1 5 0z"/></svg>your place company</li>
      <li><svg viewBox="0 0 10 10"><circle cx="5" cy="5" r="4.5"/></svg>www.yourwebsite.com</li>
    </ul>
    <div class="person"><div class="person__name">YOUR NAME</div><div class="person__role">JOB DESCRIPTION</div></div>
  </section>

  <section class="card card--back-a">
    <div class="back__band"></div>
    <div class="back__tab"><div class="back__url">www.yourwebsite.com</div></div>
    <div class="brand"><span class="brand__name">VELUNEX</span><span class="brand__unit">Research</span></div>
    <div class="back__foot"></div>
  </section>

  <section class="card card--back-b">
    <div class="back__band"></div>
    <div class="back__tab"><div class="back__url">www.yourwebsite.com</div></div>
    <div class="brand"><span class="brand__name">VELUNEX</span><span class="brand__unit">Media</span></div>
    <div class="back__foot"></div>
  </section>

</div>
</body>
</html>
```